Bright Meadow Care Partners, LLC

We are private duty home care agency. We provide in-home care for people of all ages. Our kind natured and patient caregivers provide assistance to those who have difficulty with caring for themselves. We already have a logo designed by ArtNestly

```html
<!DOCTYPE html>
<html lang="en">
<head>
<meta charset="utf-8">
<title>Bright Meadow Care Partners, LLC</title>
<link href="https://fonts.googleapis.com/css2?family=Poppins:ital,wght@0,300;0,400;0,500;0,600;0,700;1,300&display=swap" rel="stylesheet">
<style>
:root{
  --orange:#f47a0f;
  --green:#3e9b0b;
  --green-dark:#2f7f05;
  --ink:#2b2b2b;
  --text:#555;
  --muted:#999;
  --line:#e6e6e6;
  --soft:#f5f6f8;
  --footer:#4a4646;
  --white:#fff;
}
*{box-sizing:border-box;margin:0;padding:0}
html,body{width:1200px;height:4412px;overflow:hidden}
body{position:relative;font-family:"Poppins",sans-serif;color:var(--text);background:var(--white)}
.abs{position:absolute}
a{color:inherit;text-decoration:none}
.photo{position:absolute}

/* top bar */
.topbar{left:0;top:0;width:1200px;height:32px;border-bottom:1px solid #f0f0f0;font-size:12px;color:#444}
.topbar .contact{left:89px;top:8px;display:flex;gap:28px}
.topbar .contact span{display:flex;align-items:center;gap:7px}
.topbar .social{right:89px;top:8px;display:flex;gap:12px}
.topbar .social i{display:block;width:12px;height:12px;border-radius:50%;background:#b5b5b5}

/* header */
.brand{left:89px;top:58px;font-size:30px;font-weight:700;color:var(--green);display:flex;align-items:center;gap:8px;letter-spacing:-.5px}
.brand .dot{width:14px;height:14px;background:var(--orange);border-radius:50%}
.nav{right:89px;top:74px;display:flex;gap:37px;font-size:12px;font-weight:500;color:#333;letter-spacing:.3px}
.nav .active{position:relative}
.nav .active:before{content:"";position:absolute;left:10px;top:-16px;width:16px;height:3px;background:#333}

/* hero */
.hero{left:0;top:132px;width:1200px;height:664px;overflow:hidden;border-bottom-left-radius:640px 330px;
  background:linear-gradient(120deg,#c9c3bb 0%,#8a8c93 35%,#5a6b86 60%,#3b3f4c 100%)}
.hero .shade{position:absolute;inset:0;background:rgba(30,35,50,.28)}
.hero h1{position:absolute;left:0;right:0;top:228px;text-align:center;color:var(--white);font-size:56px;font-weight:600;line-height:64px}
.hero p{position:absolute;left:0;right:0;top:371px;text-align:center;color:var(--white);font-size:14px}
.hero .down{position:absolute;left:568px;top:424px;width:64px;height:42px;border-radius:21px;background:var(--orange)}
.slides{right:0;top:412px;font-size:13px;font-weight:600;color:var(--white)}
.slides div{height:40px;padding-left:0;position:relative;width:45px}
.slides .on:after{content:"";position:absolute;left:38px;top:9px;width:12px;height:2px;background:var(--orange)}

/* headings */
.h2{font-size:37px;font-weight:600;color:#333;line-height:42px}
.rule{height:3px;background:#ddd;width:58px}
.btn{display:inline-flex;align-items:center;justify-content:center;background:var(--orange);color:var(--white);font-size:11px;font-weight:600;border-radius:24px;letter-spacing:.3px;box-shadow:0 6px 14px rgba(244,122,15,.3)}

/* services */
.services-intro{left:89px;top:1005px;width:330px}
.services-intro .rule{margin:12px 0 0 -34px;width:58px}
.services-intro p{font-size:14px;line-height:22px;margin-top:26px;color:#555}
.services-intro .btn{margin-top:22px;width:182px;height:46px}
.svc{top:902px;width:301px}
.svc .photo{position:relative;height:322px;border-radius:8px}
.svc h3{margin-top:22px;font-size:16px;font-weight:600;color:#333}
.svc p{margin-top:12px;font-size:12.5px;line-height:20px;width:240px;color:#555}
.divider{left:89px;top:1411px;width:1022px;height:1px;background:var(--line)}

/* caregivers */
.care-photo{left:114px;top:1499px;width:446px;height:446px;border-radius:50%;background:linear-gradient(135deg,#ece8e2,#a7a39c 45%,#3c3b40);box-shadow:0 30px 50px rgba(0,0,0,.15)}
.care-photo-small{left:92px;top:1753px;width:194px;height:194px;border-radius:50%;border:6px solid var(--white);background:linear-gradient(135deg,#dcdcdc,#6b6b6b 60%,#2d2d2d);box-shadow:0 12px 26px rgba(0,0,0,.25)}
.care-text{left:659px;top:1528px;width:455px}
.care-text .rule{margin:12px 0 0 -34px}
.care-text p{font-size:13px;line-height:24px;margin-top:24px;color:#555}
.care-text p+p{margin-top:16px}
.care-text .btn{margin-top:24px;width:204px;height:44px}

/* interviews */
.interviews{left:0;top:2042px;width:1110px;height:637px;overflow:hidden;border-bottom-right-radius:520px 470px;
  background:linear-gradient(120deg,#46a80d 0%,#3a9608 50%,#348d07 100%)}
.interviews .leaf{position:absolute;border-radius:50%;background:rgba(255,255,255,.06)}
.icard{top:2169px;width:281px;height:384px;background:var(--white);border-radius:8px;padding:8px}
.icard .photo{position:relative;height:198px;border-radius:8px}
.icard .tag{position:absolute;left:20px;top:170px;font-size:10px;font-weight:600;color:var(--white);background:rgba(0,0,0,.35);padding:2px 8px}
.icard .meta{margin:18px 8px 0;font-size:10px;color:#aaa}
.icard h4{margin:16px 8px 0;font-size:15px;font-weight:600;color:#333}
.icard p{margin:8px 8px 0;font-size:11.5px;line-height:17px;color:#555}
.icard .go{position:absolute;right:24px;bottom:22px;width:50px;height:34px;border-radius:17px;background:var(--white);box-shadow:0 4px 10px rgba(0,0,0,.12);display:flex;align-items:center;justify-content:center}
.icard .go.hot{background:var(--orange)}
.int-title{left:717px;top:2268px;color:var(--white);font-size:37px;font-weight:600;line-height:35px}
.int-title .rule{background:rgba(255,255,255,.8);margin:22px 0 0 -18px}
.int-arrows{left:715px;top:2406px;display:flex;gap:8px}
.int-arrows span{width:34px;height:34px;border-radius:50%;border:2px solid var(--white);display:flex;align-items:center;justify-content:center}
.int-arrows span.fill{background:var(--white)}

/* clients */
.clients-title{left:0;top:2758px;width:1200px;text-align:center}
.clients-title .rule{margin:16px auto 0;width:46px}
.quote-mark{left:89px;top:2893px;font-family:"Poppins",sans-serif;font-size:300px;font-weight:700;line-height:240px;color:#fdeee3}
.quote{left:89px;top:3022px;width:530px;font-size:17px;font-style:italic;font-weight:300;line-height:36px;color:#555}
.quote-by{left:89px;top:3180px;font-size:14px;font-weight:600;color:var(--orange)}
.quote-nav{left:86px;top:3225px}
.avatar{position:absolute;border-radius:50%;border:3px solid var(--white);box-shadow:0 8px 18px rgba(0,0,0,.15)}

/* articles */
.articles-bg{left:0;top:3347px;width:1200px;height:700px;background:var(--soft);border-top-left-radius:720px 520px}
.articles-title{left:0;top:3406px;width:1200px;text-align:center}
.articles-title .rule{margin:16px auto 0;width:46px}
.post{top:3501px;width:308px;height:370px;background:var(--white);box-shadow:0 10px 30px rgba(0,0,0,.06)}
.post .photo{position:relative;height:205px}
.post .meta{margin:30px 34px 0;font-size:11px;color:#999}
.post h4{margin:14px 34px 0;font-size:15.5px;font-weight:600;line-height:25px;color:#333}
.post .more{margin:14px 34px 0;font-size:11px;font-weight:600;color:var(--orange);display:flex;align-items:center;gap:6px}

/* footer */
.footer{left:0;top:3985px;width:1200px;height:427px;background:var(--footer);border-top-left-radius:320px 260px;color:var(--white)}
.footer .brand-f{position:absolute;left:171px;top:152px;font-size:34px;font-weight:700;color:var(--white);display:flex;align-items:center;gap:10px}
.footer .brand-f .dot{width:16px;height:16px;border-radius:50%;background:var(--white)}
.footer .circles{position:absolute;left:222px;top:218px;display:flex;gap:8px}
.footer .circles i{width:28px;height:28px;border-radius:50%;display:block}
.fcol{position:absolute;top:76px}
.fcol h5{font-size:15px;font-weight:500;margin-bottom:18px}
.fcol li{list-style:none;font-size:11.5px;line-height:26.5px}
.fcol .info{font-size:11.5px;line-height:20px;display:flex;gap:8px;margin-bottom:12px}
.copyright{left:0;top:4368px;width:1200px;text-align:center;font-size:11px;font-weight:600;color:var(--white)}
.to-top{left:1138px;top:4330px;width:36px;height:36px;border-radius:50%;background:var(--orange);display:flex;align-items:center;justify-content:center}
</style>
</head>
<body>

<!-- top bar -->
<div class="abs topbar">
  <div class="abs contact">
    <span><svg width="11" height="11" viewBox="0 0 24 24"><path fill="#444" d="M6.6 10.8a15 15 0 0 0 6.6 6.6l2.2-2.2c.3-.3.7-.4 1-.2 1.1.4 2.3.6 3.6.6.6 0 1 .4 1 1V20c0 .6-.4 1-1 1A17 17 0 0 1 3 4c0-.6.4-1 1-1h3.5c.6 0 1 .4 1 1 0 1.3.2 2.5.6 3.6.1.3 0 .7-.2 1z"/></svg>555-201-7730</span>
    <span><svg width="12" height="10" viewBox="0 0 24 18"><rect width="24" height="18" rx="2" fill="#444"/><path d="M2 2l10 8 10-8" stroke="#fff" stroke-width="2" fill="none"/></svg>hello@brightmeadowcare.com</span>
  </div>
  <div class="abs social" aria-label="Social links"><i></i><i></i><i></i><i></i><i></i></div>
</div>

<!-- header -->
<div class="abs brand"><span class="dot"></span>Bright Meadow</div>
<nav class="abs nav">
  <a class="active">HOME</a><a>ABOUT</a><a>SERVICE</a><a>CAREGIVERS</a><a>INTERVIEWS</a><a>BLOG</a><a>CONTACT US</a>
</nav>

<!-- hero -->
<section class="abs hero">
  <div class="photo" role="img" aria-label="Caregiver sitting with an elderly woman holding a cane on a sofa" style="inset:0;background:linear-gradient(120deg,#d6d0c8 0%,#8e8f95 35%,#5b6c88 60%,#3a3e4b 100%)"></div>
  <div class="shade"></div>
  <h1>Live Independently in<br>your own home!</h1>
  <p>We provide in-home care for people of all ages call to receive FREE in-home assessment</p>
  <div class="down"><svg width="64" height="42" viewBox="0 0 64 42"><path d="M32 14v13M27 22l5 5 5-5" stroke="#fff" stroke-width="2" fill="none"/></svg></div>
</section>
<div class="abs slides" style="left:1149px">
  <div>01</div><div class="on">02</div><div>03</div>
</div>

<!-- services -->
<section>
  <div class="abs services-intro">
    <h2 class="h2">Our Services</h2>
    <div class="rule"></div>
    <p>Aenean sollicitudin, lorem quis bibendum nisi elit consequat ipsum nec...</p>
    <a class="btn">VIEW ALL SERVICES</a>
  </div>
  <div class="abs svc" style="left:481px">
    <div class="photo" role="img" aria-label="Caregiver holding the hands of a seated senior" style="background:linear-gradient(160deg,#6f86a6,#3f5470 55%,#7a5a3a)"></div>
    <h3>Companion and personal Care</h3>
    <p>Aenean sollicitudin, lorem quis bibendum nisi elit consequat ipsum nec dummy text...</p>
  </div>
  <div class="abs svc" style="left:808px">
    <div class="photo" role="img" aria-label="Nurse helping an elderly woman walk with a walker" style="background:linear-gradient(160deg,#d9cdb9,#9a8e7e 50%,#5b7396)"></div>
    <h3>Exceptional one on one care</h3>
    <p>Aenean sollicitudin, lorem quis bibendum nisi elit consequat ipsum nec dummy text...</p>
  </div>
  <div class="abs divider"></div>
</section>

<!-- caregivers -->
<section>
  <div class="abs care-photo" role="img" aria-label="Caregiver chatting with a smiling senior man"></div>
  <div class="abs care-photo-small" role="img" aria-label="Elderly woman looking out a window"></div>
  <div class="abs care-text">
    <h2 class="h2">In-home private duty<br>caregivers</h2>
    <div class="rule"></div>
    <p>At the Bright Meadow Care Partners, LLC we believe that a small group of caring and dedicated people create a dynamic culture that transforms lives</p>
    <p>We provide in-home care for people of all ages. Our kind natured and patient caregivers provide assistance to those who have difficulty with caring for themselves.</p>
    <a class="btn">LEARN MORE ABOUT US</a>
  </div>
</section>

<!-- interviews -->
<section class="abs interviews" role="img" aria-label="Green tinted photo of a caregiver with a senior">
  <div class="leaf" style="left:620px;top:-80px;width:420px;height:420px"></div>
  <div class="leaf" style="left:80px;top:320px;width:380px;height:380px"></div>
</section>
<div class="abs icard" style="left:-238px">
  <div class="photo" style="background:linear-gradient(135deg,#b8a38a,#5a4a3c)"></div>
</div>
<div class="abs icard" style="left:68px">
  <div class="photo" role="img" aria-label="Caregiver hugging an elderly woman" style="background:linear-gradient(135deg,#6e6a66,#c9c4c0 60%,#9fb4c6)"></div>
  <span class="tag">FULL TIME</span>
  <div class="meta">Every Wed: 09:00 am - 11:00 am</div>
  <h4>Some Heading Here...</h4>
  <p>Aenean sollicitudin, lorem quis bibendum auctor nisi elit consequat...</p>
  <div class="go hot"><svg width="16" height="12" viewBox="0 0 16 12"><path d="M1 6h13M9 1l5 5-5 5" stroke="#fff" stroke-width="1.6" fill="none"/></svg></div>
</div>
<div class="abs icard" style="left:370px">
  <div class="photo" role="img" aria-label="Senior woman and young caregiver smiling together" style="background:linear-gradient(135deg,#e6e2dd,#9aa2ae 55%,#6d7f98)"></div>
  <span class="tag">PART TIME</span>
  <div class="meta">Every Wed: 09:00 am - 11:00 am</div>
  <h4>Some Heading goes Here...</h4>
  <p>Aenean sollicitudin, lorem quis bibendum auctor nisi elit consequat...</p>
  <div class="go"><svg width="16" height="12" viewBox="0 0 16 12"><path d="M1 6h13M9 1l5 5-5 5" stroke="#222" stroke-width="1.6" fill="none"/></svg></div>
</div>
<div class="abs int-title">Some our<br>open interviews<div class="rule"></div></div>
<div class="abs int-arrows">
  <span><svg width="14" height="12" viewBox="0 0 14 12"><path d="M13 6H2M6 1L1 6l5 5" stroke="#fff" stroke-width="1.6" fill="none"/></svg></span>
  <span class="fill"><svg width="14" height="12" viewBox="0 0 14 12"><path d="M1 6h11M8 1l5 5-5 5" stroke="#222" stroke-width="1.6" fill="none"/></svg></span>
</div>

<!-- clients -->
<section>
  <div class="abs clients-title"><h2 class="h2">Clients say about</h2><div class="rule"></div></div>
  <div class="abs quote-mark" aria-hidden="true">&ldquo;</div>
  <p class="abs quote">he Lakeview Home Line has been a critical component in our campaign game plans for years, and it is a major reason why we are now Ravenshire's winningest conservative consultants.</p>
  <div class="abs quote-by">- DANA WHITLOW</div>
  <svg class="abs quote-nav" width="90" height="24" viewBox="0 0 90 24"><path d="M26 12H4M10 6l-6 6 6 6" stroke="#999" stroke-width="1.6" fill="none"/><path d="M42 12h40M76 6l6 6-6 6" stroke="#333" stroke-width="1.8" fill="none"/></svg>
  <div role="img" aria-label="Client portraits">
    <div class="avatar" style="left:830px;top:2872px;width:32px;height:32px;background:#c9b8a5"></div>
    <div class="avatar" style="left:1016px;top:2835px;width:36px;height:36px;background:#aab6c6"></div>
    <div class="avatar" style="left:881px;top:2966px;width:48px;height:48px;background:#6d5a4a"></div>
    <div class="avatar" style="left:976px;top:2926px;width:130px;height:130px;background:linear-gradient(135deg,#b88760,#3b3a40)"></div>
    <div class="avatar" style="left:743px;top:3029px;width:84px;height:84px;background:#5a4a44"></div>
    <div class="avatar" style="left:993px;top:3081px;width:60px;height:60px;background:#8c9db2"></div>
    <div class="avatar" style="left:854px;top:3092px;width:100px;height:100px;background:linear-gradient(135deg,#3fb8c0,#c88d6c)"></div>
    <div class="avatar" style="left:1036px;top:3174px;width:36px;height:36px;background:#6b6b6b"></div>
    <div class="avatar" style="left:806px;top:3210px;width:52px;height:52px;background:#b89a82"></div>
  </div>
</section>

<!-- articles -->
<div class="abs articles-bg"></div>
<section>
  <div class="abs articles-title"><h2 class="h2">Latest Article</h2><div class="rule"></div></div>
  <article class="abs post" style="left:125px">
    <div class="photo" role="img" aria-label="Senior hands resting on a wooden cane" style="background:linear-gradient(135deg,#c8ccd3,#7b8aa0 55%,#8c6a4a)"></div>
    <div class="meta">by Morgan K &nbsp;•&nbsp; 17 hours ago</div>
    <h4>Blog 1 heading: Some Blog heading goes here...</h4>
    <div class="more">LEARN MORE <svg width="16" height="10" viewBox="0 0 16 10"><path d="M1 5h13M10 1l4 4-4 4" stroke="#f47a0f" stroke-width="1.4" fill="none"/></svg></div>
  </article>
  <article class="abs post" style="left:452px">
    <div class="photo" role="img" aria-label="Young hands holding elderly hands" style="background:linear-gradient(135deg,#8a95a6,#4d5766 60%,#c4a28a)"></div>
    <div class="meta">by Morgan K &nbsp;•&nbsp; 17 hours ago</div>
    <h4>Blog 2 heading: Some Blog heading goes here...</h4>
    <div class="more">LEARN MORE <svg width="16" height="10" viewBox="0 0 16 10"><path d="M1 5h13M10 1l4 4-4 4" stroke="#f47a0f" stroke-width="1.4" fill="none"/></svg></div>
  </article>
  <article class="abs post" style="left:779px">
    <div class="photo" role="img" aria-label="Elderly man sitting with a cane" style="background:linear-gradient(135deg,#bfc2c6,#6f7478 55%,#4a4e57)"></div>
    <div class="meta">by Morgan K &nbsp;•&nbsp; 17 hours ago</div>
    <h4>Blog 3 heading: Some Blog heading goes here...</h4>
    <div class="more">LEARN MORE <svg width="16" height="10" viewBox="0 0 16 10"><path d="M1 5h13M10 1l4 4-4 4" stroke="#f47a0f" stroke-width="1.4" fill="none"/></svg></div>
  </article>
</section>

<!-- footer -->
<footer class="abs footer">
  <div class="brand-f"><span class="dot"></span>Bright Meadow</div>
  <div class="circles" aria-label="Social links">
    <i style="background:#3b5998"></i><i style="background:#1da1f2"></i><i style="background:#dd4b39"></i><i style="background:#c13584"></i>
  </div>
  <div class="fcol" style="left:510px">
    <h5>Quick Links</h5>
    <ul><li>Home</li><li>About</li><li>Our Service</li><li>Caregivers</li><li>Interviews</li><li>Blog</li><li>Contact Us</li></ul>
  </div>
  <div class="fcol" style="left:707px">
    <h5>Information</h5>
    <ul><li>Site Map</li><li>Terms &amp; Condition</li><li>Privacy Policy</li><li>FAQ's</li><li>Customer Service</li><li>Disclaimer</li></ul>
  </div>
  <div class="fcol" style="left:888px">
    <h5>Contact Information</h5>
    <div class="info"><svg width="10" height="13" viewBox="0 0 10 13"><path d="M5 0a5 5 0 0 0-5 5c0 3.5 5 8 5 8s5-4.5 5-8a5 5 0 0 0-5-5z" fill="#f47a0f"/><circle cx="5" cy="5" r="1.8" fill="#4a4646"/></svg><div>Address:<br>Some address line goes here</div></div>
    <div class="info"><svg width="10" height="10" viewBox="0 0 24 24"><path fill="#f47a0f" d="M6.6 10.8a15 15 0 0 0 6.6 6.6l2.2-2.2c.3-.3.7-.4 1-.2 1.1.4 2.3.6 3.6.6.6 0 1 .4 1 1V20c0 .6-.4 1-1 1A17 17 0 0 1 3 4c0-.6.4-1 1-1h3.5c.6 0 1 .4 1 1 0 1.3.2 2.5.6 3.6.1.3 0 .7-.2 1z"/></svg><div>Phone:<br>555-201-7730</div></div>
    <div class="info"><svg width="11" height="9" viewBox="0 0 24 18"><rect width="24" height="18" rx="2" fill="#f47a0f"/></svg><div>Email:<br>hello@brightmeadowcare.com</div></div>
  </div>
</footer>
<div class="abs copyright">© 2019, ALL RIGHTS RESERVED.</div>
<div class="abs to-top"><svg width="12" height="14" viewBox="0 0 12 14"><path d="M6 13V2M1 6l5-5 5 5" stroke="#fff" stroke-width="1.6" fill="none"/></svg></div>

</body>
</html>
```